Signage setout with photos for side of Mowing Trailer

We need signage for our mowing trailer to attract new business.
Specifically a Rear sign 1470x880mm and Side signs 2400x880mm
Sign needs to be modern and professional.
Some example uploads as to what we have thought about so far.
Logo doesn't need to be the green colour.
Logo words and Logo of Mower do not need to be together.
Link to get a mower image>
https://brightfieldgear.example/tandem
Updates

Need extra days to review

Target Market(s)

Other Customers driving past the trailer.

Industry/Entity Type

Lawnmowing / Landscaping

Requirements
Must have
• Phone Number, Company Name & Logo, Web address, Chatterlane and Pixo Logos, Comment - "Acreage & Commercial Specialists" Catchcry - "100% Electric Mowing Company - est 2017" Services "Mowing, Hedging, Pressure Cleaning, Weed Control, Fencing, Turfing, Mulching and Rubbish Removal"
Nice to have
• Full colour background images.

```html
<!DOCTYPE html>
<html lang="en">
<head>
<meta charset="utf-8">
<title>Verdant Mowing – Trailer Signage Setout</title>
<link href="https://fonts.googleapis.com/css2?family=Montserrat:wght@800&family=Oswald:wght@600&family=Poppins:wght@400;500;600;700&display=swap" rel="stylesheet">
<style>
  :root {
    --board: #dcdcdc;
    --ink: #1d1d1d;
    --white: #ffffff;
    --green: #138a3e;
    --green-dark: #0f7a36;
    --orange: #ec6a24;
    --sky: #cfe5f1;
    --lawn: #5f9f2f;
    --lawn-deep: #3d7d22;
    --rule: #555555;
  }
  * { box-sizing: border-box; margin: 0; padding: 0; }
  html, body { width: 1149px; height: 1200px; overflow: hidden; }
  body {
    background: radial-gradient(ellipse at center, #e4e4e4 0%, var(--board) 75%);
    font-family: "Poppins", sans-serif;
    color: var(--ink);
    position: relative;
  }
  .sign {
    position: absolute;
    left: 85px;
    width: 980px;
    overflow: hidden;
    background: var(--white);
    box-shadow: 0 4px 14px rgba(0,0,0,0.18);
  }
  .sign--rear { top: 60px; height: 588px; }
  .sign--side { top: 733px; height: 359px; }

  .sign__scene {
    position: absolute;
    top: 0; right: 0; bottom: 0;
    background: linear-gradient(180deg, var(--sky) 0%, #e4eef0 22%, #7fae4a 42%, var(--lawn) 70%, var(--lawn-deep) 100%);
    -webkit-mask-image: linear-gradient(90deg, transparent 0%, rgba(0,0,0,0.6) 25%, #000 45%);
    mask-image: linear-gradient(90deg, transparent 0%, rgba(0,0,0,0.6) 25%, #000 45%);
  }
  .sign--rear .sign__scene { left: 300px; }
  .sign--side .sign__scene { left: 460px; }

  .sign__band { position: absolute; left: 0; top: 0; width: 100%; height: 100%; }

  .headline {
    position: absolute;
    font-family: "Montserrat", sans-serif;
    font-weight: 800;
    text-transform: uppercase;
    color: var(--ink);
    white-space: nowrap;
  }
  .sign--rear .headline { left: 38px; top: 30px; font-size: 50px; line-height: 51px; letter-spacing: -2px; }
  .sign--side .headline { left: 32px; top: 20px; font-size: 35px; line-height: 38px; letter-spacing: -1.6px; }

  .divider { position: absolute; height: 1px; background: var(--rule); }
  .divider::after {
    content: ""; position: absolute; top: -2px; height: 5px; background: var(--orange); border-radius: 2px;
  }
  .sign--rear .divider { left: 42px; top: 202px; width: 430px; }
  .sign--rear .divider::after { left: 32px; width: 60px; }
  .sign--side .divider { left: 34px; top: 104px; width: 430px; }
  .sign--side .divider::after { left: 28px; width: 50px; }

  .claim__figure {
    position: absolute;
    font-family: "Oswald", sans-serif;
    font-weight: 600;
    color: var(--orange);
    letter-spacing: -3px;
    white-space: nowrap;
  }
  .sign--rear .claim__figure { left: 38px; top: 208px; font-size: 70px; line-height: 84px; }
  .sign--side .claim__figure { left: 32px; top: 118px; font-size: 64px; line-height: 70px; }

  .claim__text { position: absolute; font-weight: 600; color: var(--ink); white-space: nowrap; letter-spacing: 0.5px; }
  .sign--rear .claim__text { left: 206px; top: 216px; font-size: 28px; line-height: 37px; }
  .sign--side .claim__text { left: 34px; top: 188px; font-size: 21px; line-height: 27px; }

  .services__divider {
    position: absolute; left: 256px; top: 130px; height: 107px;
    border-left: 1px dotted var(--rule);
  }

  .services__tag {
    position: absolute;
    background: var(--green);
    color: var(--white);
    font-weight: 600;
    text-transform: uppercase;
    letter-spacing: 1px;
    border-radius: 0 999px 999px 0;
    white-space: nowrap;
  }
  .sign--rear .services__tag { left: 45px; top: 300px; width: 212px; height: 40px; font-size: 21px; line-height: 40px; padding-left: 13px; }
  .sign--side .services__tag { left: 269px; top: 129px; width: 139px; height: 26px; font-size: 14px; line-height: 26px; padding-left: 9px; border-radius: 4px 999px 999px 4px; }

  .services__list { position: absolute; list-style: none; display: grid; grid-auto-flow: column; }
  .service { display: flex; align-items: center; font-weight: 600; white-space: nowrap; letter-spacing: 0.4px; }
  .service__tick { flex: none; }
  .sign--rear .services__list { left: 45px; top: 350px; grid-template-rows: repeat(3, 28.5px); grid-template-columns: 116px 212px auto; }
  .sign--rear .service { font-size: 19px; gap: 7px; }
  .sign--rear .service__tick { width: 13px; height: 13px; }
  .sign--rear .service--offset { transform: translateY(3px); }
  .sign--side .services__list { left: 269px; top: 160px; grid-template-rows: repeat(4, 20.5px); grid-template-columns: 104px auto; }
  .sign--side .service { font-size: 16px; gap: 5px; }
  .sign--side .service__tick { width: 11px; height: 11px; }

  .contact { position: absolute; color: var(--white); white-space: nowrap; }
  .contact__row { display: flex; align-items: center; }
  .contact__phone { font-weight: 700; letter-spacing: 1px; }
  .contact__follow { font-weight: 400; letter-spacing: 0.5px; }
  .contact__social { display: inline-flex; align-items: center; font-weight: 500; gap: 4px; }
  .contact__social::before { content: ""; display: inline-block; background: var(--white); border-radius: 3px; }
  .contact__web { font-weight: 600; letter-spacing: 0.3px; }
  .sign--rear .contact { left: 47px; top: 498px; }
  .sign--rear .contact__row--phone { gap: 10px; height: 44px; }
  .sign--rear .contact__phone { font-size: 34px; }
  .sign--rear .contact__follow { font-size: 18px; margin-left: 6px; }
  .sign--rear .contact__social { font-size: 15px; margin-left: 6px; }
  .sign--rear .contact__social::before { width: 12px; height: 12px; }
  .sign--rear .contact__row--web { gap: 12px; height: 34px; }
  .sign--rear .contact__web { font-size: 26px; }
  .sign--rear .contact__icon { width: 24px; height: 24px; }
  .sign--side .contact { left: 34px; top: 290px; }
  .sign--side .contact__row--phone { gap: 8px; height: 30px; }
  .sign--side .contact__phone { font-size: 25px; }
  .sign--side .contact__follow { font-size: 14px; margin-left: 6px; }
  .sign--side .contact__social { font-size: 12px; margin-left: 4px; }
  .sign--side .contact__social::before { width: 10px; height: 10px; }
  .sign--side .contact__row--web { gap: 9px; height: 24px; }
  .sign--side .contact__web { font-size: 20px; }
  .sign--side .contact__icon { width: 18px; height: 18px; }

  .brand { position: absolute; display: flex; flex-direction: column; align-items: center; }
  .brand__dot { border-radius: 50%; background: var(--orange); }
  .brand__name {
    font-family: "Poppins", sans-serif;
    font-weight: 600;
    color: var(--green-dark);
    text-transform: uppercase;
    text-align: center;
  }
  .sign--rear .brand { left: 764px; top: 48px; width: 160px; gap: 14px; }
  .sign--rear .brand__dot { width: 44px; height: 44px; }
  .sign--rear .brand__name { font-size: 25px; line-height: 28px; }
  .sign--side .brand { left: 806px; top: 22px; width: 140px; gap: 9px; }
  .sign--side .brand__dot { width: 30px; height: 30px; }
  .sign--side .brand__name { font-size: 19px; line-height: 21px; }

  .size-label {
    position: absolute; left: 0; width: 100%;
    text-align: center;
    font-family: "Poppins", sans-serif;
    font-weight: 500;
    font-size: 27px;
    color: #2b2b2b;
    letter-spacing: 0.5px;
  }
  .size-label--rear { top: 663px; }
  .size-label--side { top: 1106px; }
</style>
</head>
<body>

<svg width="0" height="0" style="position:absolute">
  <defs>
    <symbol id="tick" viewBox="0 0 16 16">
      <circle cx="8" cy="8" r="8" fill="#ec6a24"/>
      <path d="M4.6 8.2 L7 10.5 L11.4 5.8" fill="none" stroke="#fff" stroke-width="2" stroke-linecap="round" stroke-linejoin="round"/>
    </symbol>
    <symbol id="phone" viewBox="0 0 24 24">
      <path d="M6.6 2.5c.5 0 .9.3 1.1.7l1.6 3.6c.2.5.1 1-.3 1.4L7.3 9.9c1.2 2.6 3.3 4.7 5.9 5.9l1.7-1.7c.4-.4.9-.5 1.4-.3l3.6 1.6c.5.2.7.6.7 1.1v3.2c0 .8-.6 1.4-1.4 1.4C10.5 21.1 2.9 13.5 2.9 4.8c0-.8.6-1.4 1.4-1.4z" fill="#ec6a24"/>
      <path d="M14.5 3.5a6 6 0 0 1 6 6M14.5 6.5a3 3 0 0 1 3 3" fill="none" stroke="#ec6a24" stroke-width="1.6" stroke-linecap="round"/>
    </symbol>
    <symbol id="globe" viewBox="0 0 24 24">
      <g fill="none" stroke="#ec6a24" stroke-width="1.8">
        <circle cx="12" cy="12" r="10"/>
        <ellipse cx="12" cy="12" rx="4.2" ry="10"/>
        <path d="M2 12h20M3.5 7h17M3.5 17h17"/>
      </g>
    </symbol>
  </defs>
</svg>

<!-- Rear sign 1470x880mm -->
<section class="sign sign--rear">
  <div class="sign__scene" role="img" aria-label="Photo of a bright green electric zero-turn ride-on mower on a mown lawn with trees and sky behind"></div>

  <svg class="sign__band" viewBox="0 0 980 588" preserveAspectRatio="none" aria-hidden="true">
    <path d="M0 506 C90 468 190 448 320 447 C500 446 640 500 780 540 C860 562 930 540 980 478 V588 H0 Z" fill="var(--orange)"/>
    <path d="M0 517 C90 481 190 462 320 461 C500 460 640 512 790 552 C870 572 935 560 980 530 V588 H0 Z" fill="var(--white)"/>
    <path d="M0 526 C90 492 190 474 320 473 C500 472 640 522 800 562 C880 580 940 576 980 558 V588 H0 Z" fill="var(--green)"/>
  </svg>

  <h1 class="headline">Acreage &amp;<br>Commercial<br>Specialists</h1>
  <div class="divider"></div>

  <div class="claim__figure">100%</div>
  <p class="claim__text">Electric Mowing<br>Company - est 2017</p>

  <div class="services__tag">Our Services</div>
  <ul class="services__list">
    <li class="service"><svg class="service__tick"><use href="#tick"/></svg>Mowing</li>
    <li class="service"><svg class="service__tick"><use href="#tick"/></svg>Hedging</li>
    <li class="service"><svg class="service__tick"><use href="#tick"/></svg>Fencing</li>
    <li class="service"><svg class="service__tick"><use href="#tick"/></svg>Pressure Cleaning</li>
    <li class="service"><svg class="service__tick"><use href="#tick"/></svg>Weed Control</li>
    <li class="service"><svg class="service__tick"><use href="#tick"/></svg>Rubbish Removal</li>
    <li class="service"><svg class="service__tick"><use href="#tick"/></svg>Turfing</li>
    <li class="service service--offset"><svg class="service__tick"><use href="#tick"/></svg>Mulching</li>
  </ul>

  <div class="contact">
    <div class="contact__row contact__row--phone">
      <svg class="contact__icon"><use href="#phone"/></svg>
      <span class="contact__phone">3555 0142</span>
      <span class="contact__follow">follow us</span>
      <span class="contact__social">Chatterlane</span>
      <span class="contact__social">Pixo</span>
    </div>
    <div class="contact__row contact__row--web">
      <svg class="contact__icon"><use href="#globe"/></svg>
      <span class="contact__web">www.verdantmowing.example</span>
    </div>
  </div>

  <div class="brand">
    <span class="brand__dot"></span>
    <span class="brand__name">Verdant<br>Mowing</span>
  </div>
</section>
<p class="size-label size-label--rear">1470x880mm</p>

<!-- Side sign 2400x880mm -->
<section class="sign sign--side">
  <div class="sign__scene" role="img" aria-label="Photo of a bright green electric zero-turn ride-on mower on a mown lawn with trees and sky behind"></div>

  <svg class="sign__band" viewBox="0 0 980 359" preserveAspectRatio="none" aria-hidden="true">
    <path d="M0 296 C60 270 150 254 260 254 C400 254 520 290 660 318 C800 340 920 320 980 245 V359 H0 Z" fill="var(--orange)"/>
    <path d="M0 305 C60 279 150 263 260 263 C400 263 520 299 670 328 C810 350 925 338 980 270 V359 H0 Z" fill="var(--white)"/>
    <path d="M0 311 C60 285 150 270 260 270 C400 270 520 305 680 335 C820 355 930 350 980 283 V359 H0 Z" fill="var(--green)"/>
  </svg>

  <h2 class="headline">Acreage &amp;<br>Commercial Specialists</h2>
  <div class="divider"></div>

  <div class="claim__figure">100%</div>
  <p class="claim__text">Electric Mowing<br>Company - est 2017</p>

  <div class="services__divider"></div>
  <div class="services__tag">Our Services</div>
  <ul class="services__list">
    <li class="service"><svg class="service__tick"><use href="#tick"/></svg>Mowing</li>
    <li class="service"><svg class="service__tick"><use href="#tick"/></svg>Hedging</li>
    <li class="service"><svg class="service__tick"><use href="#tick"/></svg>Turfing</li>
    <li class="service"><svg class="service__tick"><use href="#tick"/></svg>Mulching</li>
    <li class="service"><svg class="service__tick"><use href="#tick"/></svg>Pressure Cleaning</li>
    <li class="service"><svg class="service__tick"><use href="#tick"/></svg>Rubbish Removal</li>
    <li class="service"><svg class="service__tick"><use href="#tick"/></svg>Fencing</li>
    <li class="service"><svg class="service__tick"><use href="#tick"/></svg>Weed Control</li>
  </ul>

  <div class="contact">
    <div class="contact__row contact__row--phone">
      <svg class="contact__icon"><use href="#phone"/></svg>
      <span class="contact__phone">3555 0142</span>
      <span class="contact__follow">follow us</span>
      <span class="contact__social">Chatterlane</span>
      <span class="contact__social">Pixo</span>
    </div>
    <div class="contact__row contact__row--web">
      <svg class="contact__icon"><use href="#globe"/></svg>
      <span class="contact__web">www.verdantmowing.example</span>
    </div>
  </div>

  <div class="brand">
    <span class="brand__dot"></span>
    <span class="brand__name">Verdant<br>Mowing</span>
  </div>
</section>
<p class="size-label size-label--side">2400x880mm</p>

</body>
</html>
```